Whey Protein Packet Label Design

Company background:

Company name: Fernwick Vale

Website: fernwickvale-example.com

Summary: We offer single serving supplements on the go that are all natural. We are all about healthy living and portable packaging that makes it easy to drink anywhere. Our Whey Protein Packet saves time and is convenient for our customers to make a protein shake anywhere, there is no prep time, cook time, or clean up time. These protein packets can be added into any shaker and it is easily mixed, no more large bulk tubs of protein needed anymore because we offer single servings that are manageable to carry around.

Style: Our company name is Fernwick Vale, so in our logo we are saying that anyone can reach the mountain peak by taking healthy foods. That somehow needs to be shown through a pattern or something.

Products: Whey Protein Packets, Energy Sticks, Recovery Sticks

Product Label Instruction:

I need a product label for the Whey Protein Packet for 5 flavors.
-There should be one generic design, and the flavors just change according to color scheme and pictures

1. Strawberry Banana Smoothie (100% Organic Fruit Powder)
color scheme: Red, white, brown
2. Peanut Butter Smoothie (100% Organic Nut Powder)
color scheme: light brown, brown, white
3. Chocolate Smoothie(100% Organic Cacao Powder)
color scheme: dark brown, brown, white
4. Vanilla Shake (100% Pure Vanilla Powder)
color scheme: light cream, brown, white
5. Banana Peanut Butter Shake (100% Organic Fruit & Nut Powder)
color scheme: yellow, brown, white

Each flavor label design should have this text/information on the front:

1. Logo (attached) - does not need to be main part of design( just placed somewhere is fine)
2. Natural Whey Protein Packet (product title)
3. Flavor Name
4. Flavor Picture
5. 30G (amount of protein in each packet)
6. 4 professional stamps that easily state (attached an image for example)
1. Non GMO
2. Gluten Free
3. Lactose Free
4. No Artificial Flavoring
7. Net Weight 36G

Colors: I would like to use flavor color, brown, and white mainly for the packaging but I am open to different colors for diff flavors and colorful pictures.

Ideas: Please give me multiple designs to look at for the first draft.

Other company examples: I have attached some pictures of other packaging designs that I like that you can keep in mind.

Target Market(s)

Upscale, organic lifestyle, vegans, on the go people, police force, outdoor people, health junkies, gym goers, men and women

I hope you can make something that will appeal to most or all of these categories.

Industry/Entity Type

It Company

Requirements
Must have
• label dimensions: 3 x 3.75
• font: Unique, not something basic that looks like it came off of word document. It needs to look professional and unique that the upscale market would like.
Nice to have
• I have attached some examples of other companies that I like the look of. That is the type of style I am going for.
Should not have
• It should not be a basic design that I can make myself. I am looking for a professional who can make the product look like an organic style and shows that we offer HIGH QUALITY, high end supplements.

```html
<!DOCTYPE html>
<html lang="en">
<head>
<meta charset="utf-8">
<title>Fernwick Vale – Natural Whey Protein Packet Label</title>
<link href="https://fonts.googleapis.com/css2?family=Oswald:wght@300;400;500;600;700&display=swap" rel="stylesheet">
<style>
  :root {
    --brand-red: #c8232c;
    --deep-red: #a3151d;
    --warm-brown: #c06a3a;
    --dark-brown: #8a4322;
    --white: #ffffff;
    --page: #ffffff;
  }
  * { margin: 0; padding: 0; box-sizing: border-box; }
  html, body {
    width: 721px; height: 1200px; overflow: hidden;
    background: var(--page);
    font-family: "Oswald", sans-serif;
  }
  .canvas { position: relative; width: 721px; height: 1200px; }

  .brand-mark {
    position: absolute; top: 76px; left: 0; width: 100%;
    text-align: center;
    color: var(--brand-red);
    font-weight: 300;
    font-size: 54px;
    letter-spacing: 5px;
  }

  .label {
    position: absolute; left: 221px; top: 226px;
    width: 276px; height: 362px;
    overflow: hidden;
    background: var(--white);
  }
  .label-shapes, .label-band { position: absolute; inset: 0; width: 276px; height: 362px; }

  .label-brand {
    position: absolute; left: 10px; top: 8px;
    color: var(--brand-red);
    font-weight: 400; font-size: 17px; letter-spacing: 1.5px;
  }

  .product-photo {
    position: absolute; left: 140px; top: 52px;
    width: 94px; height: 228px;
    border-radius: 14px 14px 20px 20px;
    background: linear-gradient(180deg, #f6d2bc 0%, #efa482 40%, #e07b57 100%);
  }
  .fruit-photo {
    position: absolute; left: 6px; top: 232px;
    width: 146px; height: 56px;
    border-radius: 28px;
    background: linear-gradient(90deg, #c8232c 0%, #f2e4b0 50%, #c8232c 100%);
  }
  .fruit-photo.right {
    left: 236px; top: 232px; width: 40px; height: 40px;
  }

  .product-title {
    position: absolute; left: 10px; top: 96px;
    color: var(--white);
    font-weight: 600; font-size: 15px; line-height: 1;
  }
  .product-subtitle {
    position: absolute; left: 10px; top: 118px;
    color: var(--white);
    font-weight: 500; font-size: 11px; letter-spacing: 0.3px;
  }
  .claims {
    position: absolute; left: 10px; top: 143px;
    list-style: none;
    color: var(--white);
    font-weight: 500; font-size: 10px; line-height: 14px;
  }
  .claims li::before { content: "▸ "; }

  .flavor-band {
    position: absolute; left: 8px; top: 318px;
    width: 260px;
    transform: rotate(-9deg);
    transform-origin: left top;
    color: var(--white);
  }
  .flavor-name {
    display: block;
    font-weight: 600; font-size: 17px; line-height: 1;
  }
  .flavor-note {
    position: absolute; left: 124px; top: 21px;
    font-weight: 600; font-size: 12px; line-height: 1;
  }
  .stamps { position: absolute; left: 160px; top: 330px; display: flex; gap: 8px; }
  .stamp {
    width: 18px; height: 18px; border-radius: 50%;
    background: var(--white);
    box-shadow: inset 0 0 0 3px var(--white), inset 0 0 0 4px var(--brand-red);
  }
  .net-weight {
    position: absolute; left: 214px; top: 334px;
    color: var(--white);
    font-weight: 500; font-size: 11px;
  }
</style>
</head>
<body>
<main class="canvas">
  <div class="brand-mark">FERNWICK VALE</div>

  <section class="label" aria-label="Strawberry banana smoothie protein packet label">
    <svg class="label-shapes" viewBox="0 0 276 362" aria-hidden="true">
      <defs>
        <linearGradient id="label-bg" x1="0" y1="0" x2="0" y2="1">
          <stop offset="0" stop-color="#c9703d"/>
          <stop offset="1" stop-color="#8a4322"/>
        </linearGradient>
      </defs>
      <path d="M0 74 C90 52 180 78 276 38 L276 362 L0 362 Z" fill="url(#label-bg)"/>
      <path d="M0 52 C90 28 180 52 276 0 L276 30 C180 70 90 44 0 66 Z" fill="var(--brand-red)"/>
    </svg>

    <div class="label-brand">FERNWICK VALE</div>

    <div class="product-photo" role="img" aria-label="Photo of a strawberry banana smoothie in a tall glass with whipped cream and a straw"></div>
    <div class="fruit-photo" role="img" aria-label="Photo of fresh strawberries and banana slices"></div>
    <div class="fruit-photo right" role="img" aria-label="Photo of a fresh strawberry"></div>

    <svg class="label-band" viewBox="0 0 276 362" aria-hidden="true">
      <path d="M0 294 C90 284 190 270 276 254 L276 261 C190 277 90 291 0 301 Z" fill="var(--white)"/>
      <path d="M0 303 C90 293 190 279 276 263 L276 362 L0 362 Z" fill="var(--brand-red)"/>
    </svg>

    <h1 class="product-title">PROTEIN PACKET</h1>
    <p class="product-subtitle">NATURAL WHEY</p>
    <ul class="claims">
      <li>30G</li>
      <li>NON GMO</li>
      <li>GLUTEN FREE</li>
      <li>LACTOSE FREE</li>
      <li>NO ARTIFICIAL FLAVORING</li>
    </ul>

    <div class="flavor-band">
      <span class="flavor-name">STRAWBERRY BANANA SMOOTHIE</span>
      <span class="flavor-note">100% ORGANIC FRUIT</span>
    </div>
    <div class="stamps" aria-hidden="true"><span class="stamp"></span><span class="stamp"></span></div>
    <div class="net-weight">NET WT: 36G</div>
  </section>
</main>
</body>
</html>
```